Copperleaf Motorized Shade Business Card

Hello, we've had our logo made. Now we are looking for a clean and cool looking business card. One side can just be the logo with any design elements that might look good with it. The other side will be Name, Phone Number and Email. There will not be an address on the card.

```html
<!DOCTYPE html>
<html lang="en">
<head>
<meta charset="utf-8">
<title>Copperleaf Motorized Shades – Business Card</title>
<link rel="stylesheet" href="https://fonts.googleapis.com/css2?family=Oswald:wght@600&family=Poppins:wght@400;600&display=swap">
<style>
  :root {
    --page-bg: #26282b;
    --navy: #0d3b78;
    --sky: #00a8e8;
    --deep-blue: #003570;
    --white: #ffffff;
    --card-shadow: 0 14px 34px rgba(0,0,0,.45);
  }
  * { margin: 0; padding: 0; box-sizing: border-box; }
  html, body {
    width: 1200px; height: 900px; overflow: hidden;
    background: var(--page-bg);
  }
  .sheet {
    position: relative; width: 1200px; height: 900px;
    display: flex; flex-direction: column; align-items: center;
    justify-content: center; gap: 28px;
  }
  .card {
    position: relative; width: 680px; height: 388px;
    border-radius: 30px; box-shadow: var(--card-shadow); overflow: hidden;
  }
  .card--front {
    background: linear-gradient(200deg, var(--sky) 0%, #0077c2 45%, var(--deep-blue) 100%);
    display: flex; align-items: center; justify-content: center;
  }
  .card--back { background: var(--white); }

  .brand {
    display: flex; align-items: center; gap: 14px;
    font-family: "Poppins", sans-serif; font-weight: 600;
  }
  .brand__mark { width: 22px; height: 22px; }
  .brand__name { font-size: 34px; letter-spacing: .02em; line-height: 1; }
  .brand--light { color: var(--white); }
  .brand--light .brand__mark { background: var(--white); }
  .brand--dark { color: var(--navy); position: absolute; left: 60px; top: 150px; }
  .brand--dark .brand__mark { background: var(--navy); }
  .brand__tag { display: block; font-size: 14px; letter-spacing: .32em; margin-top: 8px; }

  .contact {
    position: absolute; right: 56px; bottom: 70px;
    text-align: right; color: var(--navy);
    font-family: "Poppins", sans-serif;
  }
  .contact__name {
    font-family: "Oswald", sans-serif; font-weight: 600;
    font-size: 30px; letter-spacing: .03em; text-transform: uppercase;
    margin-bottom: 4px;
  }
  .contact__line {
    display: flex; justify-content: flex-end; align-items: center; gap: 10px;
    font-size: 17px; line-height: 1.6;
  }
  .contact__icon { width: 16px; height: 16px; fill: var(--sky); }
</style>
</head>
<body>
<main class="sheet">
  <section class="card card--front" aria-label="Card front">
    <div class="brand brand--light">
      <span class="brand__mark"></span>
      <span class="brand__name">Copperleaf Motorized Shades</span>
    </div>
  </section>

  <section class="card card--back" aria-label="Card back">
    <div class="brand brand--dark">
      <span class="brand__mark"></span>
      <span class="brand__name">Copperleaf Motorized Shades</span>
    </div>

    <div class="contact">
      <p class="contact__name">Daniel Whitcombe</p>
      <p class="contact__line">214-555-0187
        <svg class="contact__icon" viewBox="0 0 24 24" aria-hidden="true"><path d="M6.6 10.8a15.1 15.1 0 0 0 6.6 6.6l2.2-2.2c.3-.3.7-.4 1-.2 1.1.4 2.3.6 3.6.6.6 0 1 .4 1 1V20c0 .6-.4 1-1 1C10.6 21 3 13.4 3 4c0-.6.4-1 1-1h3.5c.6 0 1 .4 1 1 0 1.3.2 2.5.6 3.6.1.3 0 .7-.2 1z"/></svg>
      </p>
      <p class="contact__line">dan@copperleafshades.com
        <svg class="contact__icon" viewBox="0 0 24 24" aria-hidden="true"><path d="M2 5h20v14H2z M3.5 6.5 12 13l8.5-6.5" fill="none" stroke="#00a8e8" stroke-width="2"/></svg>
      </p>
    </div>
  </section>
</main>
</body>
</html>
```